I need a better looking dashboard for my web application

I have a very table heavy web page that I would like to add a design touch to it. I have the logo and primary colors picked out, I just need some help in adding visual appeal the page. I would also like to add a couple of button to the page as shortcuts. Every spot that has a + sign could have a button added. I would also like to add another graph (the data will be in the uploaded files. Please feel free to ask any questions :-)

```html
<!DOCTYPE html>
<html lang="en">
<head>
<meta charset="utf-8">
<title>Dashboard UI Design : Light and Dark theme</title>
<link rel="stylesheet" href="https://fonts.googleapis.com/css2?family=Roboto:wght@400;500;700&display=swap">
<style>
:root{
  --stage:#5b5b5b;
  --purple:#663a9c;
  --green:#3daa48;
  --red:#df2f45;
}
*{box-sizing:border-box;margin:0;padding:0}
html,body{width:999px;height:1200px;overflow:hidden}
body{background:var(--stage);font-family:'Roboto',sans-serif;position:relative}

.sheet-title{position:absolute;left:0;top:18px;width:999px;text-align:center;color:#fff;font-size:28px;font-weight:500;letter-spacing:.2px}
.sheet-title-rule{position:absolute;left:199px;top:57px;width:595px;height:1px;background:#fff}

.dash{position:absolute;left:15px;width:970px;height:546px;overflow:hidden;background:var(--page);color:var(--text)}
.dash.light{top:75px;
  --page:#ececef;--panel:#fff;--bar:#fff;--row:#f1f1f4;--text:#1e1e1e;--muted:#7a7a7a;
  --line:#d9d9de;--btn:#6a3ea3;--link:#2ea3d6;--nav-active:#4a3f9c;--input:#fff;--input-line:#e2e2e6;
  --foot:#fff;--foot-text:#555;--scroll:#c9c9cf;--brand:#5e46a8}
.dash.dark{top:637px;
  --page:#282828;--panel:#0e0e0e;--bar:#0d0d0d;--row:#232323;--text:#f1f1f1;--muted:#d0d0d0;
  --line:#3d3d3d;--btn:#1f9fe4;--link:#35a8ea;--nav-active:#38a8e8;--input:transparent;--input-line:#bdbdbd;
  --foot:#0d0d0d;--foot-text:#e4e4e4;--scroll:#555;--brand:#6d55bd}

/* top bar */
.topbar{position:absolute;left:0;top:0;width:970px;height:40px;background:var(--bar);border-bottom:1px solid var(--line)}
.brand{position:absolute;left:13px;top:10px;display:flex;align-items:center;gap:6px;color:var(--brand);font-size:19px;font-weight:500}
.brand-mark{width:14px;height:14px;background:var(--brand);border-radius:2px}
.brand-sep{position:absolute;left:151px;top:4px;width:1px;height:32px;background:var(--line)}
.nav{position:absolute;top:0;height:40px;display:flex;align-items:center;gap:5px;font-size:9.5px;color:var(--muted)}
.nav svg{width:13px;height:13px;stroke:currentColor;fill:none;stroke-width:1.4}
.nav .chev{width:7px;height:7px;stroke-width:2}
.nav.active{color:var(--nav-active);font-weight:500}
.user-mail{position:absolute;left:741px;top:0;height:40px;line-height:40px;font-size:9.5px;color:var(--muted)}
.avatar{position:absolute;left:857px;top:8px;width:24px;height:24px;border-radius:50%;background:radial-gradient(circle at 50% 40%,#b08a72,#4a3a32)}
.bar-sep{position:absolute;top:4px;width:1px;height:32px;background:var(--line)}
.bar-icon{position:absolute;top:13px;width:14px;height:14px;stroke:var(--muted);fill:none;stroke-width:1.3}

/* panels */
.panel{position:absolute;width:459px;background:var(--panel);border-radius:10px;overflow:hidden}
.p-open{left:16px;top:55px;height:202px}
.p-chart{left:494px;top:55px;height:202px}
.p-leave{left:16px;top:274px;height:202px}
.p-images{left:494px;top:274px;height:202px}
.p-mine{left:16px;top:490px;height:40px}
.p-attend{left:494px;top:490px;height:40px}
.panel-title{position:absolute;left:13px;top:8px;font-size:9.5px;font-weight:700}
.filter{position:absolute;left:304px;top:8px;width:101px;height:13px;border:1px solid var(--input-line);background:var(--input);border-radius:7px;font-size:6.5px;color:var(--muted);padding-left:8px;line-height:11px}
.btn{position:absolute;top:8px;width:12px;height:12px;border-radius:2px;background:var(--btn);display:flex;align-items:center;justify-content:center}
.btn svg{width:8px;height:8px;stroke:#fff;fill:none;stroke-width:1.8}
.btn.add{left:418px}.btn.reload{left:436px}

/* tables */
.tbl{position:absolute;left:14px;top:28px;width:430px;font-size:6.2px;font-weight:500}
.thead{display:grid;grid-template-columns:var(--cols);border-top:1px solid var(--line);font-size:7px;font-weight:500;text-align:center}
.thead span{display:flex;align-items:center;justify-content:center;height:16px}
.thead span+span{border-left:1px solid var(--line)}
.thead .span-top{border-bottom:1px solid var(--line)}
.tbody{margin-top:5px;position:relative}
.row{display:grid;grid-template-columns:var(--cols);height:18px;margin-bottom:2px;background:var(--row);border-radius:3px;align-items:stretch}
.row>span{display:flex;align-items:center;padding-left:5px;border-left:1.5px solid var(--panel);white-space:nowrap;overflow:hidden}
.row>span:first-child{border-left:none}
.row .act{gap:8px;padding-left:7px}
.ic{width:6.5px;height:6.5px;stroke:var(--text);fill:none;stroke-width:1.3}
.link{color:var(--link)}
.thumb{display:inline-block;width:10px;height:10px;border-radius:2px;margin-right:4px;flex:none;background:linear-gradient(135deg,#c9a58c,#6f5648)}
.scroll{position:absolute;left:432px;top:0;width:2px;height:72px;border-radius:1px;background:var(--scroll)}

.t-open{--cols:39px 57px 75px 43px 82px 46px 88px}
.t-leave{--cols:39px 57px 107px 57px 82px 88px}
.t-leave .thead{grid-template-rows:16px 16px}
.t-img{left:15px;width:429px;--cols:96px 106px 37px 120px 70px}
.t-img .thead{grid-template-rows:16px 16px}
.t-img .tbody{margin-top:4px;height:126px;overflow:hidden}
.t-img .row{height:30px;margin-bottom:5.4px;font-size:7px}
.t-img .row>span{padding-left:7px}
.t-img .row>span.pic{padding-left:4px}
.portrait{width:25px;height:26px;border-radius:3px;background:linear-gradient(160deg,#e7d2c4,#9c7a68)}
.opts{gap:6px;padding-left:22px!important}
.ok,.no{width:9px;height:9px;border-radius:1.5px;display:flex;align-items:center;justify-content:center}
.ok{background:var(--green)}.no{background:var(--red)}
.ok svg,.no svg{width:6px;height:6px;stroke:#fff;fill:none;stroke-width:2}

/* chart */
.chart{position:absolute;left:0;top:0;width:459px;height:202px}
.chart .axis{stroke:var(--text);stroke-width:.8}
.chart .grid{stroke:var(--line);stroke-width:.5}
.chart text{fill:var(--text);font-family:'Roboto',sans-serif}
.chart .tick{font-size:5px}
.chart .lab{font-size:4.6px}
.chart .legend{font-size:4.4px}
.chart .xtitle{font-size:7px;font-weight:500}
.b-purple{fill:var(--purple)}.b-green{fill:var(--green)}.b-red{fill:var(--red)}

.footer{position:absolute;left:0;top:516px;width:970px;height:30px;background:var(--foot);border-top:1px solid var(--line);text-align:center;line-height:30px;font-size:7px;color:var(--foot-text)}
</style>
</head>
<body>
<svg width="0" height="0" style="position:absolute">
  <defs>
    <symbol id="i-edit" viewBox="0 0 10 10"><path d="M4 1.5H1.5v7h7V6"/><path d="M7.5 1 9 2.5 5 6.5H3.5V5z"/></symbol>
    <symbol id="i-trash" viewBox="0 0 10 10"><path d="M1.5 2.5h7M4 2.5V1h2v1.5M2.5 2.5l.6 6.5h3.8l.6-6.5"/></symbol>
    <symbol id="i-eye" viewBox="0 0 10 10"><path d="M.8 5S2.5 2 5 2s4.2 3 4.2 3S7.5 8 5 8 .8 5 .8 5z"/><circle cx="5" cy="5" r="1.2"/></symbol>
    <symbol id="i-plus" viewBox="0 0 10 10"><path d="M5 1.5v7M1.5 5h7"/></symbol>
    <symbol id="i-reload" viewBox="0 0 10 10"><path d="M8 4A3.2 3.2 0 0 0 2.2 3.3M2 6a3.2 3.2 0 0 0 5.8.7"/><path d="M2 1.5v2h2M8 8.5v-2H6"/></symbol>
    <symbol id="i-tick" viewBox="0 0 10 10"><path d="M2 5.2 4.2 7.3 8 2.8"/></symbol>
    <symbol id="i-x" viewBox="0 0 10 10"><path d="M2.5 2.5l5 5M7.5 2.5l-5 5"/></symbol>
    <symbol id="i-home" viewBox="0 0 14 14"><path d="M2 6.5 7 2l5 4.5V12H8.7V8.5H5.3V12H2z"/></symbol>
    <symbol id="i-flame" viewBox="0 0 14 14"><path d="M7 1.5c.5 2.5 3.8 3.8 3.8 7A3.8 3.8 0 0 1 3.2 8.5C3.2 6.5 4.5 5.5 5 4c.6 1 1 1.5 1.6 1.8C7 4.5 7 3 7 1.5z"/></symbol>
    <symbol id="i-pin" viewBox="0 0 14 14"><path d="M7 12.5S2.8 8.5 2.8 5.6a4.2 4.2 0 0 1 8.4 0C11.2 8.5 7 12.5 7 12.5z"/><circle cx="7" cy="5.6" r="1.6"/></symbol>
    <symbol id="i-shapes" viewBox="0 0 14 14"><path d="M7 1.5 9.5 5.5h-5z"/><rect x="1.8" y="8" width="4" height="4"/><circle cx="10" cy="10" r="2"/></symbol>
    <symbol id="i-chev" viewBox="0 0 8 8"><path d="M1.5 3 4 5.5 6.5 3"/></symbol>
    <symbol id="i-bell" viewBox="0 0 14 14"><path d="M3.5 10V6.5a3.5 3.5 0 0 1 7 0V10l1 1h-9zM5.8 12.5h2.4"/></symbol>
    <symbol id="i-gear" viewBox="0 0 14 14"><circle cx="7" cy="7" r="2"/><path d="M7 1.3l1.1 1.4 1.7-.4.4 1.7 1.6.8-.7 1.6.7 1.6-1.6.8-.4 1.7-1.7-.4L7 12.7l-1.1-1.4-1.7.4-.4-1.7-1.6-.8L2.9 7.6 2.2 6l1.6-.8.4-1.7 1.7.4z"/></symbol>
  </defs>
</svg>

<h1 class="sheet-title">Dashboard UI Design : Light and Dark theme</h1>
<div class="sheet-title-rule"></div>

<!-- ============ LIGHT THEME ============ -->
<section class="dash light">
  <header class="topbar">
    <div class="brand"><span class="brand-mark"></span>ShiftCover</div>
    <div class="brand-sep"></div>
    <div class="nav active" style="left:160px"><svg><use href="#i-home"/></svg>Home</div>
    <div class="nav" style="left:229px"><svg><use href="#i-flame"/></svg>Demo Outbox</div>
    <div class="nav" style="left:316px"><svg><use href="#i-pin"/></svg>Location Admin<svg class="chev"><use href="#i-chev"/></svg></div>
    <div class="nav" style="left:425px"><svg><use href="#i-shapes"/></svg>Regular Staff<svg class="chev"><use href="#i-chev"/></svg></div>
    <div class="user-mail">dn.manager@example.com</div>
    <div class="avatar" role="img" aria-label="Signed-in manager profile photo"></div>
    <div class="bar-sep" style="left:889px"></div>
    <svg class="bar-icon" style="left:908px"><use href="#i-bell"/></svg>
    <div class="bar-sep" style="left:930px"></div>
    <svg class="bar-icon" style="left:949px"><use href="#i-gear"/></svg>
  </header>

  <article class="panel p-open">
    <h2 class="panel-title">Managed Openings</h2>
    <div class="filter">Enter Filter Keywords..</div>
    <div class="btn add"><svg><use href="#i-plus"/></svg></div>
    <div class="btn reload"><svg><use href="#i-reload"/></svg></div>
    <div class="tbl t-open">
      <div class="thead"><span></span><span>Category</span><span>Regular Staff</span><span>Status</span><span>Summary</span><span>Location</span><span>Time Slots Summary</span></div>
      <div class="tbody">
        <div class="scroll"></div>
        <div class="row"><span class="act"><svg class="ic"><use href="#i-edit"/></svg><svg class="ic"><use href="#i-trash"/></svg></span><span class="link">Food Service</span><span>Extra duty</span><span class="link">Assigned</span><span>Immediate Need! Library</span><span class="link">LJE</span><span>12/30 - 01/01 (2h 10m)</span></div>
        <div class="row"><span class="act"><svg class="ic"><use href="#i-edit"/></svg><svg class="ic"><use href="#i-trash"/></svg></span><span class="link">Teacher</span><span>Naoimi Willis</span><span class="link">Available</span><span>Immediate Need! Library</span><span class="link">LJE</span><span>12/30 - 01/01 (2h 10m)</span></div>
        <div class="row"><span class="act"><svg class="ic"><use href="#i-edit"/></svg><svg class="ic"><use href="#i-trash"/></svg></span><span class="link">Bus Driver</span><span>Extra duty</span><span class="link">Available</span><span>Immediate Need! Library</span><span class="link">LJE</span><span>12/30 - 01/01 (2h 10m)</span></div>
        <div class="row"><span class="act"><svg class="ic"><use href="#i-edit"/></svg><svg class="ic"><use href="#i-trash"/></svg></span><span class="link">Custodian</span><span>Extra duty</span><span class="link">Available</span><span>Immediate Need! Library</span><span class="link">LJE</span><span>12/30 - 01/01 (2h 10m)</span></div>
        <div class="row"><span class="act"><svg class="ic"><use href="#i-edit"/></svg><svg class="ic"><use href="#i-trash"/></svg></span><span class="link">Teacher's Aide</span><span>Extra duty</span><span class="link">Available</span><span>Immediate Need! Library</span><span class="link">LJE</span><span>12/30 - 01/01 (2h 10m)</span></div>
        <div class="row"><span class="act"><svg class="ic"><use href="#i-edit"/></svg><svg class="ic"><use href="#i-trash"/></svg></span><span class="link">Food Service</span><span>Gladys Richardson</span><span class="link">Available</span><span>Immediate Need! Library</span><span class="link">LJE</span><span>12/30 - 01/01 (2h 10m)</span></div>
        <div class="row"><span class="act"><svg class="ic"><use href="#i-edit"/></svg><svg class="ic"><use href="#i-trash"/></svg></span><span class="link">Teacher's Aide</span><span>Alan Bowman</span><span class="link">Available</span><span>Immediate Need! Library</span><span class="link">LJE</span><span>12/30 - 01/01 (2h 10m)</span></div>
      </div>
    </div>
  </article>

  <article class="panel p-chart">
    <h2 class="panel-title">Location Overview</h2>
    <svg class="chart" viewBox="0 0 459 202">
      <g class="grid"><line x1="27" y1="51.3" x2="441" y2="51.3"/><line x1="27" y1="71.6" x2="441" y2="71.6"/><line x1="27" y1="91.9" x2="441" y2="91.9"/><line x1="27" y1="112.2" x2="441" y2="112.2"/><line x1="27" y1="132.4" x2="441" y2="132.4"/><line x1="27" y1="152.7" x2="441" y2="152.7"/></g>
      <line class="axis" x1="27" y1="38" x2="27" y2="173"/>
      <line class="axis" x1="27" y1="173" x2="441" y2="173"/>
      <g class="tick" text-anchor="end"><text x="21" y="53">12</text><text x="21" y="73">10</text><text x="21" y="94">8</text><text x="21" y="114">6</text><text x="21" y="134">4</text><text x="21" y="155">2</text><text x="21" y="175">0</text></g>
      <rect class="b-purple" x="53" y="142.6" width="15" height="30.4"/><rect class="b-green" x="53" y="132.4" width="15" height="10.2"/><rect class="b-red" x="74" y="132.4" width="15" height="40.6"/>
      <rect class="b-purple" x="139" y="122.3" width="15" height="50.7"/><rect class="b-red" x="160" y="132.4" width="15" height="40.6"/>
      <rect class="b-purple" x="225" y="112.2" width="15" height="60.8"/><rect class="b-red" x="246" y="71.6" width="15" height="101.4"/>
      <rect class="b-purple" x="311" y="122.3" width="15" height="50.7"/><rect class="b-red" x="331" y="132.4" width="15" height="40.6"/>
      <g class="lab" text-anchor="middle"><text x="71" y="181">Lake Jonas Elementary</text><text x="157" y="181">Feestberg Middle School</text><text x="243" y="181">West Devante Middle School</text><text x="329" y="182.5">East Devante Middle School</text></g>
      <text class="xtitle" x="229" y="193" text-anchor="middle">LeaveRequest/Openings/Assignments</text>
      <g class="legend"><rect class="b-purple" x="253" y="33" width="4.5" height="4.5"/><text x="260" y="37">Opening : Unfilled</text><rect class="b-green" x="323" y="33" width="4.5" height="4.5"/><text x="330" y="37">Opening : filled</text><rect class="b-red" x="376" y="33" width="4.5" height="4.5"/><text x="383" y="37">LeaveRequest : Pending</text></g>
    </svg>
  </article>

  <article class="panel p-leave">
    <h2 class="panel-title">Regular Staff Leave Request</h2>
    <div class="filter">Enter Filter Keywords..</div>
    <div class="btn add"><svg><use href="#i-plus"/></svg></div>
    <div class="btn reload"><svg><use href="#i-reload"/></svg></div>
    <div class="tbl t-leave">
      <div class="thead">
        <span style="grid-column:1;grid-row:1/3"></span>
        <span style="grid-column:2;grid-row:1">Status</span>
        <span style="grid-column:3;grid-row:1">Full Name</span>
        <span class="span-top" style="grid-column:4/6;grid-row:1">Openings</span>
        <span style="grid-column:4;grid-row:2">Assignments</span>
        <span style="grid-column:5;grid-row:2">Prearranged Sub</span>
        <span style="grid-column:6;grid-row:1">Time Slots Summary</span>
      </div>
      <div class="tbody">
        <div class="scroll"></div>
        <div class="row"><span class="act"><svg class="ic"><use href="#i-edit"/></svg><svg class="ic"><use href="#i-eye"/></svg></span><span>Pending</span><span class="link"><i class="thumb" role="img" aria-label="Staff photo"></i>Naoimi Willis</span><span>N/A</span><span class="link">N/A</span><span>12/30 - 01/01 (2h 10m)</span></div>
        <div class="row"><span class="act"><svg class="ic"><use href="#i-edit"/></svg><svg class="ic"><use href="#i-eye"/></svg></span><span>Pending</span><span class="link"><i class="thumb" role="img" aria-label="Staff photo"></i>Jeremy Gardner</span><span>N/A</span><span class="link">N/A</span><span>12/30 - 01/01 (2h 10m)</span></div>
        <div class="row"><span class="act"><svg class="ic"><use href="#i-edit"/></svg><svg class="ic"><use href="#i-eye"/></svg></span><span>Pending</span><span class="link"><i class="thumb" role="img" aria-label="Staff photo"></i>Scarlett Cook</span><span>Counselor</span><span class="link">N/A</span><span>12/30 - 01/01 (2h 10m)</span></div>
        <div class="row"><span class="act"><svg class="ic"><use href="#i-edit"/></svg><svg class="ic"><use href="#i-eye"/></svg></span><span>Pending</span><span class="link"><i class="thumb" role="img" aria-label="Staff photo"></i>Hannah Collins</span><span>N/A</span><span class="link">N/A</span><span>12/30 - 01/01 (2h 10m)</span></div>
        <div class="row"><span class="act"><svg class="ic"><use href="#i-edit"/></svg><svg class="ic"><use href="#i-eye"/></svg></span><span>Pending</span><span class="link"><i class="thumb" role="img" aria-label="Staff photo"></i>Gladys Richardson</span><span>Administrator</span><span class="link"><i class="thumb" role="img" aria-label="Substitute photo"></i>Ian Robertson</span><span>12/30 - 01/01 (2h 10m)</span></div>
        <div class="row"><span class="act"><svg class="ic"><use href="#i-edit"/></svg><svg class="ic"><use href="#i-eye"/></svg></span><span>Pending</span><span class="link"><i class="thumb" role="img" aria-label="Staff photo"></i>Alan Bowman</span><span>Administrator</span><span class="link">N/A</span><span>12/30 - 01/01 (2h 10m)</span></div>
      </div>
    </div>
  </article>

  <article class="panel p-images">
    <h2 class="panel-title">Pending Profile Images</h2>
    <div class="filter">Enter Filter Keywords..</div>
    <div class="btn add"><svg><use href="#i-plus"/></svg></div>
    <div class="btn reload"><svg><use href="#i-reload"/></svg></div>
    <div class="tbl t-img">
      <div class="thead">
        <span style="grid-column:1;grid-row:1">Last Name</span>
        <span style="grid-column:2;grid-row:1">First Name</span>
        <span class="span-top" style="grid-column:3/5;grid-row:1">Profile Images</span>
        <span style="grid-column:3;grid-row:2">Pending</span>
        <span style="grid-column:4;grid-row:2">Prearranged Sub</span>
        <span style="grid-column:5;grid-row:1">Options</span>
      </div>
      <div class="tbody">
        <div class="scroll" style="left:429px;height:62px"></div>
        <div class="row"><span>Walters</span><span class="link">Kim</span><span class="pic"><i class="portrait" role="img" aria-label="Pending profile photo"></i></span><span>None Available</span><span class="opts"><i class="ok"><svg><use href="#i-tick"/></svg></i><i class="no"><svg><use href="#i-x"/></svg></i></span></div>
        <div class="row"><span>Stevens</span><span class="link">Masons</span><span class="pic"><i class="portrait" role="img" aria-label="Pending profile photo"></i></span><span>None Available</span><span class="opts"><i class="ok"><svg><use href="#i-tick"/></svg></i><i class="no"><svg><use href="#i-x"/></svg></i></span></div>
        <div class="row"><span>Morales</span><span class="link">Junes</span><span class="pic"><i class="portrait" role="img" aria-label="Pending profile photo"></i></span><span>None Available</span><span class="opts"><i class="ok"><svg><use href="#i-tick"/></svg></i><i class="no"><svg><use href="#i-x"/></svg></i></span></div>
        <div class="row"><span>Stephens</span><span class="link">Priscilla</span><span class="pic"><i class="portrait" role="img" aria-label="Pending profile photo"></i></span><span>None Available</span><span class="opts"><i class="ok"><svg><use href="#i-tick"/></svg></i><i class="no"><svg><use href="#i-x"/></svg></i></span></div>
      </div>
    </div>
  </article>

  <article class="panel p-mine">
    <h2 class="panel-title">My Leave Requests</h2>
    <div class="filter">Enter Filter Keywords..</div>
    <div class="btn add"><svg><use href="#i-plus"/></svg></div>
    <div class="btn reload"><svg><use href="#i-reload"/></svg></div>
  </article>
  <article class="panel p-attend">
    <h2 class="panel-title">Substitute Attendance</h2>
    <div class="filter">Enter Filter Keywords..</div>
    <div class="btn add"><svg><use href="#i-plus"/></svg></div>
    <div class="btn reload"><svg><use href="#i-reload"/></svg></div>
  </article>

  <footer class="footer">Copyright Northfield Systems. All Rights Reserved. (v0.8.4)</footer>
</section>

<!-- ============ DARK THEME ============ -->
<section class="dash dark">
  <header class="topbar">
    <div class="brand"><span class="brand-mark"></span>ShiftCover</div>
    <div class="brand-sep"></div>
    <div class="nav active" style="left:160px"><svg><use href="#i-home"/></svg>Home</div>
    <div class="nav" style="left:229px"><svg><use href="#i-flame"/></svg>Demo Outbox</div>
    <div class="nav" style="left:316px"><svg><use href="#i-pin"/></svg>Location Admin<svg class="chev"><use href="#i-chev"/></svg></div>
    <div class="nav" style="left:425px"><svg><use href="#i-shapes"/></svg>Regular Staff<svg class="chev"><use href="#i-chev"/></svg></div>
    <div class="user-mail">dn.manager@example.com</div>
    <div class="avatar" role="img" aria-label="Signed-in manager profile photo"></div>
    <div class="bar-sep" style="left:889px"></div>
    <svg class="bar-icon" style="left:908px"><use href="#i-bell"/></svg>
    <div class="bar-sep" style="left:930px"></div>
    <svg class="bar-icon" style="left:949px"><use href="#i-gear"/></svg>
  </header>

  <article class="panel p-open">
    <h2 class="panel-title">Managed Openings</h2>
    <div class="filter">Enter Filter Keywords..</div>
    <div class="btn add"><svg><use href="#i-plus"/></svg></div>
    <div class="btn reload"><svg><use href="#i-reload"/></svg></div>
    <div class="tbl t-open">
      <div class="thead"><span></span><span>Category</span><span>Regular Staff</span><span>Status</span><span>Summary</span><span>Location</span><span>Time Slots Summary</span></div>
      <div class="tbody">
        <div class="scroll"></div>
        <div class="row"><span class="act"><svg class="ic"><use href="#i-edit"/></svg><svg class="ic"><use href="#i-trash"/></svg></span><span class="link">Food Service</span><span>Extra duty</span><span class="link">Assigned</span><span>Immediate Need! Library</span><span class="link">LJE</span><span>12/30 - 01/01 (2h 10m)</span></div>
        <div class="row"><span class="act"><svg class="ic"><use href="#i-edit"/></svg><svg class="ic"><use href="#i-trash"/></svg></span><span class="link">Teacher</span><span>Naoimi Willis</span><span class="link">Available</span><span>Immediate Need! Library</span><span class="link">LJE</span><span>12/30 - 01/01 (2h 10m)</span></div>
        <div class="row"><span class="act"><svg class="ic"><use href="#i-edit"/></svg><svg class="ic"><use href="#i-trash"/></svg></span><span class="link">Bus Driver</span><span>Extra duty</span><span class="link">Available</span><span>Immediate Need! Library</span><span class="link">LJE</span><span>12/30 - 01/01 (2h 10m)</span></div>
        <div class="row"><span class="act"><svg class="ic"><use href="#i-edit"/></svg><svg class="ic"><use href="#i-trash"/></svg></span><span class="link">Custodian</span><span>Extra duty</span><span class="link">Available</span><span>Immediate Need! Library</span><span class="link">LJE</span><span>12/30 - 01/01 (2h 10m)</span></div>
        <div class="row"><span class="act"><svg class="ic"><use href="#i-edit"/></svg><svg class="ic"><use href="#i-trash"/></svg></span><span class="link">Teacher's Aide</span><span>Extra duty</span><span class="link">Available</span><span>Immediate Need! Library</span><span class="link">LJE</span><span>12/30 - 01/01 (2h 10m)</span></div>
        <div class="row"><span class="act"><svg class="ic"><use href="#i-edit"/></svg><svg class="ic"><use href="#i-trash"/></svg></span><span class="link">Food Service</span><span>Gladys Richardson</span><span class="link">Available</span><span>Immediate Need! Library</span><span class="link">LJE</span><span>12/30 - 01/01 (2h 10m)</span></div>
        <div class="row"><span class="act"><svg class="ic"><use href="#i-edit"/></svg><svg class="ic"><use href="#i-trash"/></svg></span><span class="link">Teacher's Aide</span><span>Alan Bowman</span><span class="link">Available</span><span>Immediate Need! Library</span><span class="link">LJE</span><span>12/30 - 01/01 (2h 10m)</span></div>
      </div>
    </div>
  </article>

  <article class="panel p-chart">
    <h2 class="panel-title">Location Overview</h2>
    <svg class="chart" viewBox="0 0 459 202">
      <line class="axis" x1="27" y1="38" x2="27" y2="173"/>
      <line class="axis" x1="27" y1="173" x2="441" y2="173"/>
      <g class="tick" text-anchor="end"><text x="21" y="53">12</text><text x="21" y="73">10</text><text x="21" y="94">8</text><text x="21" y="114">6</text><text x="21" y="134">4</text><text x="21" y="155">2</text></g>
      <rect class="b-purple" x="53" y="142.6" width="15" height="30.4"/><rect class="b-green" x="53" y="132.4" width="15" height="10.2"/><rect class="b-red" x="74" y="132.4" width="15" height="40.6"/>
      <rect class="b-purple" x="139" y="122.3" width="15" height="50.7"/><rect class="b-red" x="160" y="132.4" width="15" height="40.6"/>
      <rect class="b-purple" x="225" y="112.2" width="15" height="60.8"/><rect class="b-red" x="246" y="71.6" width="15" height="101.4"/>
      <rect class="b-purple" x="311" y="122.3" width="15" height="50.7"/><rect class="b-red" x="331" y="132.4" width="15" height="40.6"/>
      <g class="lab" text-anchor="middle"><text x="71" y="181">Lake Jonas Elementary</text><text x="157" y="181">Feestberg Middle School</text><text x="243" y="181">West Devante Middle School</text><text x="329" y="182.5">East Devante Middle School</text></g>
      <text class="xtitle" x="229" y="193" text-anchor="middle">LeaveRequest/Openings/Assignments</text>
      <g class="legend"><rect class="b-purple" x="253" y="33" width="4.5" height="4.5"/><text x="260" y="37">Opening : Unfilled</text><rect class="b-green" x="323" y="33" width="4.5" height="4.5"/><text x="330" y="37">Opening : filled</text><rect class="b-red" x="376" y="33" width="4.5" height="4.5"/><text x="383" y="37">LeaveRequest : Pending</text></g>
    </svg>
  </article>

  <article class="panel p-leave">
    <h2 class="panel-title">Regular Staff Leave Request</h2>
    <div class="filter">Enter Filter Keywords..</div>
    <div class="btn add"><svg><use href="#i-plus"/></svg></div>
    <div class="btn reload"><svg><use href="#i-reload"/></svg></div>
    <div class="tbl t-leave">
      <div class="thead">
        <span style="grid-column:1;grid-row:1/3"></span>
        <span style="grid-column:2;grid-row:1">Status</span>
        <span style="grid-column:3;grid-row:1">Full Name</span>
        <span class="span-top" style="grid-column:4/6;grid-row:1">Openings</span>
        <span style="grid-column:4;grid-row:2">Assignments</span>
        <span style="grid-column:5;grid-row:2">Prearranged Sub</span>
        <span style="grid-column:6;grid-row:1">Time Slots Summary</span>
      </div>
      <div class="tbody">
        <div class="scroll"></div>
        <div class="row"><span class="act"><svg class="ic"><use href="#i-edit"/></svg><svg class="ic"><use href="#i-eye"/></svg></span><span>Pending</span><span class="link"><i class="thumb" role="img" aria-label="Staff photo"></i>Naoimi Willis</span><span>N/A</span><span class="link">N/A</span><span>12/30 - 01/01 (2h 10m)</span></div>
        <div class="row"><span class="act"><svg class="ic"><use href="#i-edit"/></svg><svg class="ic"><use href="#i-eye"/></svg></span><span>Pending</span><span class="link"><i class="thumb" role="img" aria-label="Staff photo"></i>Jeremy Gardner</span><span>N/A</span><span class="link">N/A</span><span>12/30 - 01/01 (2h 10m)</span></div>
        <div class="row"><span class="act"><svg class="ic"><use href="#i-edit"/></svg><svg class="ic"><use href="#i-eye"/></svg></span><span>Pending</span><span class="link"><i class="thumb" role="img" aria-label="Staff photo"></i>Scarlett Cook</span><span>Counselor</span><span class="link">N/A</span><span>12/30 - 01/01 (2h 10m)</span></div>
        <div class="row"><span class="act"><svg class="ic"><use href="#i-edit"/></svg><svg class="ic"><use href="#i-eye"/></svg></span><span>Pending</span><span class="link"><i class="thumb" role="img" aria-label="Staff photo"></i>Hannah Collins</span><span>N/A</span><span class="link">N/A</span><span>12/30 - 01/01 (2h 10m)</span></div>
        <div class="row"><span class="act"><svg class="ic"><use href="#i-edit"/></svg><svg class="ic"><use href="#i-eye"/></svg></span><span>Pending</span><span class="link"><i class="thumb" role="img" aria-label="Staff photo"></i>Gladys Richardson</span><span>Administrator</span><span class="link"><i class="thumb" role="img" aria-label="Substitute photo"></i>Ian Robertson</span><span>12/30 - 01/01 (2h 10m)</span></div>
        <div class="row"><span class="act"><svg class="ic"><use href="#i-edit"/></svg><svg class="ic"><use href="#i-eye"/></svg></span><span>Pending</span><span class="link"><i class="thumb" role="img" aria-label="Staff photo"></i>Alan Bowman</span><span>Administrator</span><span class="link">N/A</span><span>12/30 - 01/01 (2h 10m)</span></div>
      </div>
    </div>
  </article>

  <article class="panel p-images">
    <h2 class="panel-title">Pending Profile Images</h2>
    <div class="filter">Enter Filter Keywords..</div>
    <div class="btn add"><svg><use href="#i-plus"/></svg></div>
    <div class="btn reload"><svg><use href="#i-reload"/></svg></div>
    <div class="tbl t-img">
      <div class="thead">
        <span style="grid-column:1;grid-row:1">Last Name</span>
        <span style="grid-column:2;grid-row:1">First Name</span>
        <span class="span-top" style="grid-column:3/5;grid-row:1">Profile Images</span>
        <span style="grid-column:3;grid-row:2">Pending</span>
        <span style="grid-column:4;grid-row:2">Prearranged Sub</span>
        <span style="grid-column:5;grid-row:1">Options</span>
      </div>
      <div class="tbody">
        <div class="scroll" style="left:429px;height:62px"></div>
        <div class="row"><span>Walters</span><span class="link">Kim</span><span class="pic"><i class="portrait" role="img" aria-label="Pending profile photo"></i></span><span>None Available</span><span class="opts"><i class="ok"><svg><use href="#i-tick"/></svg></i><i class="no"><svg><use href="#i-x"/></svg></i></span></div>
        <div class="row"><span>Stevens</span><span class="link">Masons</span><span class="pic"><i class="portrait" role="img" aria-label="Pending profile photo"></i></span><span>None Available</span><span class="opts"><i class="ok"><svg><use href="#i-tick"/></svg></i><i class="no"><svg><use href="#i-x"/></svg></i></span></div>
        <div class="row"><span>Morales</span><span class="link">Junes</span><span class="pic"><i class="portrait" role="img" aria-label="Pending profile photo"></i></span><span>None Available</span><span class="opts"><i class="ok"><svg><use href="#i-tick"/></svg></i><i class="no"><svg><use href="#i-x"/></svg></i></span></div>
        <div class="row"><span>Stephens</span><span class="link">Priscilla</span><span class="pic"><i class="portrait" role="img" aria-label="Pending profile photo"></i></span><span>None Available</span><span class="opts"><i class="ok"><svg><use href="#i-tick"/></svg></i><i class="no"><svg><use href="#i-x"/></svg></i></span></div>
      </div>
    </div>
  </article>

  <article class="panel p-mine">
    <h2 class="panel-title">My Leave Requests</h2>
    <div class="filter">Enter Filter Keywords..</div>
    <div class="btn add"><svg><use href="#i-plus"/></svg></div>
    <div class="btn reload"><svg><use href="#i-reload"/></svg></div>
  </article>
  <article class="panel p-attend">
    <h2 class="panel-title">Substitute Attendance</h2>
    <div class="filter">Enter Filter Keywords..</div>
    <div class="btn add"><svg><use href="#i-plus"/></svg></div>
    <div class="btn reload"><svg><use href="#i-reload"/></svg></div>
  </article>

  <footer class="footer">Copyright Northfield Systems. All Rights Reserved. (v0.8.4)</footer>
</section>
</body>
</html>
```